Your Road Counsel Billboard Design for Personal Injury Law Firm

Need a billboard design that we can use for different versions. 1400px X 400px jpeg or png
I have attached the logo and the attorney for the billboard. Attorney Dana Whitfield
Here is a link to our current website yourroadcounsel-example.com

HEADLINE: HIT BY A TRUCK?
SUBHEAD: NO FEE. BIG FIGHT.
855-MARGOT-7

HEADLINE: ACCIDENT?
SUBHEAD: NO FEE, UNLESS WE WIN!
855-MARGOT-7

HEADLINE: BIG TRUCK. BIG CASE.
SUBHEAD: YOU PAY $0 UPFRONT
855-MARGOT-7

Target Market(s)

People in Car Accident

Industry/Entity Type

Personal Injury Attorneys

```html
<!DOCTYPE html>
<html lang="en">
<head>
<meta charset="utf-8">
<title>Your Road Counsel Billboard</title>
<link href="https://fonts.googleapis.com/css2?family=Montserrat:wght@700;800;900&display=swap" rel="stylesheet">
<style>
  :root {
    --brand-green: #76c04a;
    --band-gray: #48484a;
    --ink: #0b0b0b;
    --paper: #ffffff;
    --stage: #e8e9eb;
    --logo-gray: #4a4a4c;
  }
  html, body {
    margin: 0;
    padding: 0;
    width: 1200px;
    height: 400px;
    overflow: hidden;
    background: var(--stage);
  }
  .billboard {
    position: absolute;
    left: 20px;
    top: 34px;
    width: 1160px;
    height: 332px;
    display: block;
  }
  .billboard text {
    font-family: "Montserrat", sans-serif;
  }
  .headline { font-weight: 900; fill: var(--ink); }
  .subhead { font-weight: 800; fill: var(--ink); }
  .phone { font-weight: 700; fill: var(--paper); }
  .attorney-name { font-weight: 800; fill: var(--ink); }
  .firm-name { font-weight: 700; fill: var(--logo-gray); }
</style>
</head>
<body>
<svg class="billboard" viewBox="0 0 1160 332" xmlns="http://www.w3.org/2000/svg">
  <defs>
    <linearGradient id="portraitTone" x1="0" y1="0" x2="0" y2="1">
      <stop offset="0" stop-color="#c9a37a"/>
      <stop offset="0.45" stop-color="#b78a62"/>
      <stop offset="0.55" stop-color="#1f2a44"/>
      <stop offset="1" stop-color="#1a2238"/>
    </linearGradient>
  </defs>

  <!-- panel -->
  <rect class="panel" x="0" y="0" width="1160" height="332" fill="var(--paper)"/>

  <!-- attorney backdrop -->
  <rect class="attorney-backdrop" x="0" y="0" width="318" height="332" fill="var(--brand-green)"/>

  <!-- subhead band -->
  <polygon class="subhead-shadow" points="587,89 1160,89 1160,135 620,135" fill="var(--band-gray)"/>
  <polygon class="subhead-band" points="600,89 1160,89 1160,135 633,135" fill="var(--brand-green)"/>

  <!-- phone band -->
  <rect class="phone-band" x="230" y="147" width="930" height="96" fill="var(--band-gray)"/>

  <!-- name band -->
  <polygon class="name-shadow" points="300,255 620,255 652,301 300,301" fill="var(--band-gray)"/>
  <polygon class="name-band" points="300,255 608,255 640,301 300,301" fill="var(--brand-green)"/>

  <!-- attorney portrait -->
  <rect class="attorney-portrait" x="26" y="0" width="290" height="332" rx="0" fill="url(#portraitTone)" role="img" aria-label="Portrait of attorney Dana Whitfield, arms crossed, wearing a navy blazer"/>

  <!-- copy -->
  <text class="headline" x="344" y="77" font-size="60" textLength="730" lengthAdjust="spacingAndGlyphs">BIG TRUCK. BIG CASE.</text>
  <text class="subhead" x="1074" y="127" font-size="38" text-anchor="end">YOU PAY $0 UPFRONT</text>
  <text class="phone" x="344" y="233" font-size="100" textLength="730" lengthAdjust="spacingAndGlyphs">855–MARGOT–7</text>
  <text class="attorney-name" x="344" y="290" font-size="30">DANA WHITFIELD</text>

  <!-- firm mark -->
  <rect class="firm-square" x="763" y="262" width="28" height="28" fill="var(--brand-green)"/>
  <text class="firm-name" x="806" y="287" font-size="28" textLength="268" lengthAdjust="spacingAndGlyphs">YOUR ROAD COUNSEL</text>
</svg>
</body>
</html>
```